Western Canadian Survey Company needs Business Card and Letter Head Design

Hello,

We're looking to have our business cards redesigned along with our letterhead.

We've recently changed out logo and would like to use this. Please use some creativity and propose different options (Traditional and modern).

We will provide as much feedback as possible.

Business card should be double sided with our logo. We would also like room for cell phone number, email address and position. Back of the card can just be our logo or potentially a list of our services we provide.

Industry/Entity Type

Business

Contact Information for Business Card

```html
<!DOCTYPE html>
<html lang="en">
<head>
<meta charset="utf-8">
<title>Northline Field Surveys – Stationery</title>
<link rel="stylesheet" href="https://fonts.googleapis.com/css2?family=Michroma&family=Raleway:wght@300;400&display=swap">
<style>
  :root{
    --backdrop:#d1d2d4;
    --paper:#ffffff;
    --ink:#111111;
    --slate:#557788;
    --rule:#1a1a1a;
    --shadow:rgba(0,0,0,.45);
  }
  *{box-sizing:border-box;margin:0;padding:0}
  html,body{width:1200px;height:918px;overflow:hidden;background:var(--backdrop)}
  body{position:relative;font-family:"Raleway",sans-serif;color:var(--ink)}

  .sheet{position:absolute;background:var(--paper);box-shadow:10px 10px 12px var(--shadow)}

  /* Letterhead */
  .letterhead{left:37px;top:48px;width:642px;height:830px}
  .letterhead .masthead{position:absolute;left:0;right:0;top:0;height:110px;border-bottom:2px solid var(--rule);text-align:center}
  .brand{font-family:"Michroma",sans-serif;color:var(--slate);letter-spacing:1px;white-space:nowrap}
  .letterhead .brand-mark{position:absolute;top:34px;left:0;right:0;font-size:22px;color:var(--ink)}
  .letterhead .brand-name{position:absolute;top:74px;left:0;right:0;font-size:14px}
  .letterhead .footer{position:absolute;left:0;right:0;top:750px;border-top:2px solid var(--rule);text-align:center}
  .footer .icons{display:flex;justify-content:center;gap:14px;margin-top:10px}
  .footer .contact{font-size:17px;line-height:20px;margin-top:6px;font-weight:400}

  /* Business card front */
  .card-front{left:717px;top:203px;width:444px;height:253px}
  .card-front .brand-mark{position:absolute;top:70px;left:0;right:0;text-align:center;font-size:20px;color:var(--ink)}
  .card-front .brand-name{position:absolute;top:108px;left:0;right:0;text-align:center;font-size:12px}
  .card-front .id-band{position:absolute;left:0;right:0;bottom:0;height:60px;background:var(--ink);color:var(--paper)}
  .id-band .person{position:absolute;left:17px;top:14px}
  .person .name{font-family:"Michroma",sans-serif;font-size:14px;letter-spacing:.5px}
  .person .role{font-size:11px;margin-top:2px;font-weight:300}
  .id-band .accent{position:absolute;left:205px;top:12px;width:30px;height:30px;background:var(--slate)}
  .id-band .contact{position:absolute;right:15px;top:18px;font-size:9px;line-height:12px;text-align:right;font-weight:300}
  .id-band .contact span{display:flex;justify-content:flex-end;align-items:center;gap:6px}

  /* Business card back */
  .card-back{left:717px;top:471px;width:444px;height:253px;background:var(--slate);color:var(--paper);text-align:center}
  .card-back .brand-mark{position:absolute;top:84px;left:0;right:0;font-family:"Michroma",sans-serif;font-size:38px;letter-spacing:2px}
  .card-back .services{position:absolute;top:164px;left:0;right:0;font-size:11.5px;line-height:17px;font-weight:300}
</style>
</head>
<body>

<section class="sheet letterhead">
  <header class="masthead">
    <div class="brand brand-mark">NFSL</div>
    <div class="brand brand-name">NORTHLINE FIELD SURVEYS LTD</div>
  </header>
  <footer class="footer">
    <div class="icons">
      <svg width="12" height="13" viewBox="0 0 12 13" aria-label="phone"><path d="M3 1 L5 4 L4 5.5 Q5 8.5 7.5 9.5 L9 8.5 L11 10.5 L9.5 12 Q3 11 1 3 Z" fill="none" stroke="#557788" stroke-width="1.2"/></svg>
      <svg width="14" height="11" viewBox="0 0 14 11" aria-label="email"><rect x="1" y="1" width="12" height="9" fill="none" stroke="#333" stroke-width="1.2"/><path d="M1 1 L7 6 L13 1" fill="none" stroke="#333" stroke-width="1.2"/></svg>
    </div>
    <p class="contact">+1 604 555-0142<br>info@northlinefieldsurveys.com</p>
  </footer>
</section>

<section class="sheet card-front">
  <div class="brand brand-mark">NFSL</div>
  <div class="brand brand-name">NORTHLINE FIELD SURVEYS LTD</div>
  <div class="id-band">
    <div class="person">
      <div class="name">MARLA KEATING</div>
      <div class="role">DIRECTOR</div>
    </div>
    <div class="accent"></div>
    <div class="contact">
      <span>+1 604 555-0142 <svg width="7" height="8" viewBox="0 0 12 13"><path d="M3 1 L5 4 L4 5.5 Q5 8.5 7.5 9.5 L9 8.5 L11 10.5 L9.5 12 Q3 11 1 3 Z" fill="#fff"/></svg></span>
      <span>info@northlinefieldsurveys.com <svg width="8" height="7" viewBox="0 0 14 11"><rect x="1" y="1" width="12" height="9" fill="none" stroke="#fff" stroke-width="1.5"/><path d="M1 1 L7 6 L13 1" fill="none" stroke="#fff" stroke-width="1.5"/></svg></span>
    </div>
  </div>
</section>

<section class="sheet card-back">
  <div class="brand-mark">NFSL</div>
  <p class="services">QA/QC &amp; Survey Control - Construction Surveys<br>Underground Utility Location - GIS / Drafting</p>
</section>

</body>
</html>
```